New business card for UK roofing company

We are Brindmore Roofing and we need a business card design for our staff.

We offer the following services:

- New roofs
- General roof repairs
- Drone surveys
- Single ply roofing
- Steel cladding
- Asbestos removal
- Electronic leak detection

I have attached our logo. I have also attached example branding printed to our vans. The business card should fit in with the style of our branding.

The business card should have the following information;

Address:
Unit 17c Wendlecroft Farm
Wendlecroft Lane
Hatchington
CM4 9QD

Telephone: 020 7946 0372
24 Hour: 0800 612 4479

Email: ray@brindmoreroofing.example
Mobile: 07700981234
Name: Ray Tunstead
Website: www.brindmoreroofing.example

The business card will be printed in Spot UV, see here: https://www.kestaprint.example/business-cards/spot-uv/

If you need anymore info, please let me know,

```html
<!DOCTYPE html>
<html lang="en">
<head>
<meta charset="utf-8">
<title>Brindmore Roofing – Business Card</title>
<link rel="stylesheet" href="https://fonts.googleapis.com/css2?family=Fira+Sans:wght@400;600;700&display=swap">
<style>
  :root {
    --navy: #0b4a7e;
    --navy-deep: #0a3f6e;
    --ocean: #12709f;
    --cyan: #22b2df;
    --slate: #2e5a8f;
    --faint: #3163a0;
    --paper: #f8f8f7;
    --paper-shade: #c9c9c9;
    --ink: #ffffff;
    --backdrop: #2a2a2a;
  }
  * { margin: 0; padding: 0; box-sizing: border-box; }
  html, body { width: 1200px; height: 883px; overflow: hidden; }
  body {
    background: var(--backdrop);
    font-family: "Fira Sans", Arial, sans-serif;
    position: relative;
  }
  .card {
    position: absolute;
    width: 540px;
    height: 350px;
    overflow: hidden;
    box-shadow: 0 10px 30px rgba(0,0,0,.55);
  }
  /* ---------- front ---------- */
  .card--front {
    left: 40px; top: 60px;
    background: linear-gradient(150deg, var(--navy-deep) 0%, var(--navy) 55%, var(--ocean) 100%);
    color: var(--ink);
  }
  .card__decor {
    position: absolute;
    right: -70px; top: 30px;
    width: 260px; height: 260px;
  }
  .edge-marks { position: absolute; left: 24px; top: 180px; }
  .edge-marks span {
    display: block; width: 4px; height: 36px;
    background: var(--cyan); margin-bottom: 22px;
  }
  .brand {
    position: absolute; left: 60px; top: 50px;
    display: flex; align-items: center; gap: 12px;
  }
  .brand__dot {
    width: 34px; height: 34px; border-radius: 50%;
    background: var(--cyan);
  }
  .brand__name {
    font-size: 32px; font-weight: 700; letter-spacing: -0.5px; color: var(--ink);
  }
  .contact { position: absolute; left: 60px; top: 168px; }
  .contact__name { font-size: 21px; font-weight: 700; }
  .contact__line { font-size: 13px; margin-top: 2px; }
  .contact__rule {
    width: 300px; height: 2px; background: var(--cyan); margin: 5px 0 8px;
  }
  .contact__address { font-size: 13px; }
  .contact__phone { font-size: 13.5px; line-height: 1.3; }
  .contact__phone b { font-weight: 700; }
  .contact__web {
    font-size: 17px; font-weight: 700; margin-top: 22px; letter-spacing: .2px;
  }
  /* ---------- back ---------- */
  .card--back {
    left: 620px; top: 440px;
    background: linear-gradient(160deg, var(--paper) 55%, var(--paper-shade) 100%);
  }
  .card--back svg { position: absolute; inset: 0; }
  .back-brand {
    position: absolute; left: 22px; bottom: 24px;
    display: flex; align-items: center; gap: 10px;
  }
  .back-brand__dot {
    width: 34px; height: 34px; border-radius: 50%; background: var(--cyan);
  }
  .back-brand__name {
    font-size: 30px; font-weight: 700; color: var(--slate); letter-spacing: -0.5px;
  }
</style>
</head>
<body>

<section class="card card--front" aria-label="Business card front">
  <svg class="card__decor" viewBox="0 0 260 260" aria-hidden="true">
    <circle cx="130" cy="130" r="124" fill="none" stroke="var(--faint)" stroke-width="3"/>
    <circle cx="130" cy="130" r="110" fill="var(--faint)" opacity=".55"/>
  </svg>

  <div class="edge-marks" aria-hidden="true"><span></span><span></span><span></span></div>

  <div class="brand">
    <div class="brand__dot"></div>
    <div class="brand__name">Brindmore Roofing</div>
  </div>

  <div class="contact">
    <div class="contact__name">Ray Tunstead</div>
    <div class="contact__line">ray@brindmoreroofing.example | &nbsp;Mobile: 07700981234</div>
    <div class="contact__rule"></div>
    <div class="contact__address">Unit 17c Wendlecroft Farm | Wendlecroft Lane | Hatchington | CM4 9QD</div>
    <div class="contact__phone"><b>Telephone:</b> 020 7946 0372</div>
    <div class="contact__phone"><b>24 Hour:</b> 0800 612 4479</div>
    <div class="contact__web">www.brindmoreroofing.example</div>
  </div>
</section>

<section class="card card--back" aria-label="Business card back">
  <svg viewBox="0 0 540 350" aria-hidden="true">
    <path class="band-top" d="M0 0 H540 V92 C420 100 300 112 0 140 Z" fill="var(--navy)"/>
    <path class="band-stripe" d="M0 140 C300 112 420 100 540 92 V104 C400 112 200 120 0 190 Z" fill="var(--cyan)"/>
    <path class="band-edge" d="M0 190 C200 120 400 112 540 104" fill="none" stroke="var(--navy)" stroke-width="3"/>
    <circle cx="430" cy="140" r="108" fill="var(--paper)" stroke="var(--slate)" stroke-width="3"/>
    <circle cx="430" cy="140" r="92" fill="var(--cyan)"/>
  </svg>
  <div class="back-brand">
    <div class="back-brand__dot"></div>
    <div class="back-brand__name">Brindmore Roofing</div>
  </div>
</section>

</body>
</html>
```